brix4lane

i want to ues this logo and the same colors used on the business card

cleaning & service

Industry/Entity Type

Business

Contact Information for Business Card

Font styles to use
Serif
Sans Serif
Decorative
Script

Colors
add136
0692cd
000000
5c5c5c
fbfbfb

Requirements
Must have
• cleaning things

```html
<!DOCTYPE html>
<html lang="en">
<head>
<meta charset="utf-8">
<title>brix4lane – Business Card</title>
<link href="https://fonts.googleapis.com/css2?family=Kaushan+Script&family=Open+Sans:wght@400;700&display=swap" rel="stylesheet">
<style>
  :root {
    --bg: #e6e7ea;
    --card: #fbfbfb;
    --front-blue: #0b72bb;
    --back-blue: #3b55a6;
    --logo-blue: #1a6fbf;
    --green: #8cc63f;
    --ink-white: #ffffff;
  }
  html, body {
    margin: 0;
    width: 1200px;
    height: 800px;
    overflow: hidden;
    background: var(--bg);
  }
  .canvas {
    position: relative;
    width: 1200px;
    height: 800px;
  }
  .card {
    position: absolute;
    top: 257px;
    width: 500px;
    height: 286px;
    background: var(--card);
    box-shadow: 0 6px 18px rgba(0,0,0,0.14);
    overflow: hidden;
  }
  .card--front { left: 70px; }
  .card--back { left: 630px; }
  .card__waves {
    position: absolute;
    inset: 0;
    width: 100%;
    height: 100%;
  }
  .brand {
    position: absolute;
    display: flex;
    align-items: center;
    gap: 8px;
    font-family: "Open Sans", sans-serif;
    font-weight: 700;
    font-size: 26px;
    color: var(--logo-blue);
    letter-spacing: 0.5px;
  }
  .brand__dot {
    width: 14px;
    height: 14px;
    border-radius: 50%;
    background: var(--green);
  }
  .card--front .brand { left: 150px; top: 110px; }
  .card--back .brand { left: 40px; top: 56px; font-size: 22px; }
  .holder-name {
    position: absolute;
    right: 34px;
    top: 84px;
    margin: 0;
    font-family: "Kaushan Script", cursive;
    font-weight: 400;
    font-size: 34px;
    line-height: 44px;
    color: var(--logo-blue);
  }
  .holder-name__last { color: var(--green); }
  .contact {
    position: absolute;
    right: 28px;
    bottom: 24px;
    margin: 0;
    padding: 0;
    list-style: none;
    font-family: "Open Sans", sans-serif;
    font-size: 14px;
    color: var(--ink-white);
    text-align: right;
  }
  .contact__item {
    display: flex;
    align-items: center;
    justify-content: flex-end;
    gap: 8px;
    line-height: 22px;
  }
  .contact__icon { width: 14px; height: 14px; }
</style>
</head>
<body>
<main class="canvas">

  <section class="card card--front" aria-label="Card front">
    <svg class="card__waves" viewBox="0 0 500 286" preserveAspectRatio="none" aria-hidden="true">
      <path d="M0,138 C140,150 300,215 500,262" fill="none" stroke="var(--green)" stroke-width="5"/>
      <path d="M0,148 C140,160 300,226 500,270 L500,286 L470,286 C300,250 150,200 0,188 Z" fill="var(--front-blue)"/>
    </svg>
    <div class="brand"><span class="brand__dot"></span>brix4lane</div>
  </section>

  <section class="card card--back" aria-label="Card back">
    <svg class="card__waves" viewBox="0 0 500 286" preserveAspectRatio="none" aria-hidden="true">
      <path d="M0,108 C90,100 180,130 260,158 C340,184 420,182 500,178" fill="none" stroke="var(--green)" stroke-width="6"/>
      <path d="M0,120 C90,112 180,142 260,170 C340,196 420,194 500,190 L500,286 L0,286 Z" fill="var(--back-blue)"/>
      <path d="M70,140 C150,170 240,190 330,194 C390,196 440,194 480,198 C430,201 390,202 330,204 C240,204 150,184 70,140 Z" fill="var(--card)"/>
    </svg>
    <div class="brand"><span class="brand__dot"></span>brix4lane</div>
    <h1 class="holder-name">Mara <span class="holder-name__last">Quill</span></h1>
    <ul class="contact">
      <li class="contact__item">27-400-050-318
        <svg class="contact__icon" viewBox="0 0 14 14" aria-hidden="true"><rect width="14" height="14" rx="2" fill="var(--green)"/><path d="M4 3 L6 3 L6.6 5.2 L5.6 6 C6.2 7.2 6.8 7.8 8 8.4 L8.8 7.4 L11 8 L11 10 C7 10.5 3.5 7 4 3 Z" fill="#fff"/></svg>
      </li>
      <li class="contact__item">yourname@brix4lane.com
        <svg class="contact__icon" viewBox="0 0 14 14" aria-hidden="true"><rect width="14" height="14" rx="2" fill="var(--green)"/><rect x="2.5" y="4" width="9" height="6.5" fill="#fff"/><path d="M2.5 4 L7 7.6 L11.5 4" fill="none" stroke="var(--green)" stroke-width="1"/></svg>
      </li>
    </ul>
  </section>

</main>
</body>
</html>
```